Book cover entitled #GLOWBEYONDIT

Design front book cover (self-self-portait photos included) for my first book entitled -

#GLOWBEYONDIT (may be best to have different shades of colour for glow beyond it to stand off you). I'm intentionally choosing a title that is essentially a hashtag.

Subtitle - Rewriting quiet inner battles

Concept of cover - left side of my face is shaded with shame and right side is brighter and hopeful. I have also include my logo.

Link for photos
https://www.filqorvex.com/sh/tq7mxd2kw9pl41a/BBR8NpXwQ3hLm6TzvKe2YUJ5b?dl=0

Target Market(s)

People (or friends & family) suffering with the shame of mental health struggles

Industry/Entity Type

Mental Health

Font styles to use
Other font styles liked:
• Avenir

Colors
3276b5
85acd3
cfdeed

Requirements
Must have
• Relatable, contemporary, authentic & compelling
• Link for photos
• https://www.filqorvex.com/sh/tq7mxd2kw9pl41a/BBR8NpXwQ3hLm6TzvKe2YUJ5b?dl=0
Nice to have
• Abstract & creative
Should not have
• Cheesy, plastic, pedestrian etc

```html
<!DOCTYPE html>
<html lang="en">
<head>
<meta charset="utf-8">
<title>#GLOWBEYONDIT – Book Cover</title>
<link href="https://fonts.googleapis.com/css2?family=Bebas+Neue&family=Oswald:wght@400;500&display=swap" rel="stylesheet">
<style>
  :root {
    --page-bg: #f1f1f1;
    --cover-black: #050505;
    --title-yellow: #f7c81e;
    --title-blue: #2a9fdc;
    --subtitle-yellow: #f5d21d;
    --name-white: #ffffff;
    --portrait-dark: #0a0a0a;
    --portrait-shadow: #2b1d14;
    --portrait-warm: #b17b58;
    --portrait-silver: #d9d9d9;
  }
  * { margin: 0; padding: 0; box-sizing: border-box; }
  html, body {
    width: 1200px;
    height: 800px;
    overflow: hidden;
    background: var(--page-bg);
  }
  .book-cover {
    position: absolute;
    left: 390px;
    top: 40px;
    width: 420px;
    height: 720px;
    background: var(--cover-black);
    overflow: hidden;
  }
  .author-portrait {
    position: absolute;
    left: 92px;
    top: 0;
    width: 328px;
    height: 720px;
    background:
      linear-gradient(180deg, rgba(0,0,0,0) 0%, rgba(0,0,0,0) 62%, rgba(10,14,24,0.85) 82%, #0b1020 100%),
      linear-gradient(90deg, var(--portrait-dark) 0%, var(--portrait-dark) 22%, var(--portrait-shadow) 38%, var(--portrait-warm) 58%, #a37556 72%, var(--portrait-silver) 86%, #c9c9c9 100%);
  }
  .title-column {
    position: absolute;
    left: 0;
    top: 16px;
    width: 110px;
    height: 600px;
  }
  .title-text {
    font-family: "Bebas Neue", "Oswald", sans-serif;
    font-size: 136px;
  }
  .author-mark {
    position: absolute;
    left: 40px;
    top: 650px;
    display: flex;
    align-items: center;
    gap: 7px;
    font-family: "Oswald", sans-serif;
    font-weight: 400;
    font-size: 15px;
    color: var(--name-white);
    letter-spacing: 0.3px;
  }
  .author-mark .mark-dot {
    width: 12px;
    height: 12px;
    border-radius: 50%;
    background: var(--name-white);
  }
  .subtitle {
    position: absolute;
    left: 134px;
    bottom: 22px;
    font-family: "Oswald", sans-serif;
    font-weight: 500;
    font-size: 16px;
    text-transform: uppercase;
    letter-spacing: 0.4px;
    color: var(--subtitle-yellow);
  }
</style>
</head>
<body>
  <main class="book-cover">
    <div class="author-portrait" role="img" aria-label="Author portrait, face half in deep shadow on the left and lit warmly on the right against a brushed silver backdrop"></div>

    <svg class="title-column" viewBox="0 0 110 600" aria-label="#GLOWBEYONDIT">
      <defs>
        <linearGradient id="titleGradient" gradientUnits="userSpaceOnUse" x1="0" y1="0" x2="575" y2="0">
          <stop offset="0" stop-color="#f7c81e"/>
          <stop offset="0.40" stop-color="#f4c620"/>
          <stop offset="0.56" stop-color="#cfd86e"/>
          <stop offset="0.72" stop-color="#62c7ee"/>
          <stop offset="1" stop-color="#2a9fdc"/>
        </linearGradient>
      </defs>
      <text class="title-text" transform="translate(102,588) rotate(-90)" x="0" y="0"
            textLength="575" lengthAdjust="spacingAndGlyphs" fill="url(#titleGradient)">#GLOWBEYONDIT</text>
    </svg>

    <div class="author-mark">
      <span class="mark-dot"></span>
      <span class="author-name">dale corwin</span>
    </div>

    <p class="subtitle">Rewriting quiet inner battles</p>
  </main>
</body>
</html>
```